Business Card Design

We need a business card for a new business based in Sydney, Australia. It is a home based baking business, the key products are cookies and muffins and slices including gluten free baked goods. With the emphasis on home made baking. The target market is cafes, coffee shops and vans, restaurants. Products may be provided in display jars or individually wrapped. The final design should be in the colours pink, purple.

Industry/Entity Type

Business

Contact Information for Business Card

Pindle's Bakery Pty Ltd, Maren Tulloch, maren@pindlesbakery.com.au
0412 506 218, www.pindlesbakery.com.au, ACN 581 246 037,

```html
<!DOCTYPE html>
<html lang="en">
<head>
<meta charset="utf-8">
<title>Pindle's Bakery Pty Ltd – Business Card</title>
<link rel="stylesheet" href="https://fonts.googleapis.com/css2?family=Open+Sans:wght@400;600&family=Cormorant+Garamond:ital,wght@1,600&display=swap">
<style>
  :root {
    --page-bg: #f2f2f2;
    --card-pink: #e0187f;
    --band-purple: #7d3393;
    --frame-purple: #7a3a98;
    --frame-fill: #f7f5fa;
    --logo-ink: #6b2c86;
    --text-light: #ffffff;
    --stitch: #c9b6d6;
  }
  * { box-sizing: border-box; margin: 0; padding: 0; }
  html, body {
    width: 1200px; height: 900px; overflow: hidden;
    background: var(--page-bg);
  }
  .business-card {
    position: absolute; left: 100px; top: 150px;
    width: 1000px; height: 600px;
    border-radius: 42px; overflow: hidden;
    background: var(--card-pink);
    box-shadow: 0 18px 40px rgba(0,0,0,0.18);
  }
  .accent-band {
    position: absolute; left: 0; right: 0; top: 200px; height: 150px;
    background: var(--band-purple);
    border-top: 5px solid var(--text-light);
    border-bottom: 5px solid var(--text-light);
  }
  .owner-name {
    position: absolute; right: 52px; top: 62px;
    font-family: "Cormorant Garamond", serif; font-style: italic; font-weight: 600;
    font-size: 34px; color: var(--text-light);
  }
  .logo-frame {
    position: absolute; left: 230px; top: 100px; width: 480px; height: 350px;
  }
  .logo-frame svg { position: absolute; inset: 0; }
  .logo-lockup {
    position: absolute; inset: 0;
    display: flex; flex-direction: column; align-items: center; justify-content: center;
    font-family: "Open Sans", sans-serif; font-weight: 600; color: var(--logo-ink);
    text-align: center;
  }
  .logo-name { font-size: 58px; line-height: 1.1; }
  .logo-entity { font-size: 34px; line-height: 1.3; }
  .baker-illustration {
    position: absolute; left: 760px; top: 215px; width: 230px; height: 400px;
    border-radius: 110px 110px 0 0;
    background: linear-gradient(180deg, #e6c26c 0%, #f1cdb6 35%, #d64a93 55%, #8a46a6 100%);
  }
  .contact-list {
    position: absolute; left: 50px; top: 460px; list-style: none;
    font-family: "Open Sans", sans-serif; font-weight: 600; color: var(--text-light);
    font-size: 25px; line-height: 34px;
  }
  .contact-list li { display: flex; align-items: center; gap: 10px; }
  .contact-list svg { width: 30px; height: 30px; flex: none; }
  .contact-list .company-number {
    font-weight: 400; font-size: 19px; padding-left: 40px; line-height: 28px;
  }
</style>
</head>
<body>
  <div class="business-card">
    <div class="accent-band"></div>
    <p class="owner-name">Maren Tulloch</p>

    <div class="logo-frame">
      <svg viewBox="0 0 480 350" aria-hidden="true">
        <path d="M60 40 Q60 20 90 20 L390 20 Q420 20 420 40 Q420 60 450 60 Q470 60 470 90 L470 260 Q470 290 450 290 Q420 290 420 310 Q420 330 390 330 L90 330 Q60 330 60 310 Q60 290 30 290 Q10 290 10 260 L10 90 Q10 60 30 60 Q60 60 60 40 Z"
              fill="var(--frame-fill)" stroke="var(--frame-purple)" stroke-width="14"/>
        <path d="M68 48 Q70 32 92 32 L388 32 Q410 32 412 48 Q416 72 448 72 Q458 74 458 92 L458 258 Q458 276 448 278 Q416 278 412 302 Q410 318 388 318 L92 318 Q70 318 68 302 Q64 278 32 278 Q22 276 22 258 L22 92 Q22 74 32 72 Q64 72 68 48 Z"
              fill="none" stroke="var(--stitch)" stroke-width="2" stroke-dasharray="7 5"/>
      </svg>
      <div class="logo-lockup">
        <span class="logo-name">Pindle's</span>
        <span class="logo-entity">Bakery Pty Ltd</span>
      </div>
    </div>

    <div class="baker-illustration" role="img" aria-label="Illustration of a smiling baker in a purple apron holding a plate of chocolate cookies"></div>

    <ul class="contact-list">
      <li>
        <svg viewBox="0 0 24 24" aria-hidden="true"><path fill="#fff" d="M6.6 10.8a15.1 15.1 0 0 0 6.6 6.6l2.2-2.2a1 1 0 0 1 1-.25 11.4 11.4 0 0 0 3.6.57 1 1 0 0 1 1 1V20a1 1 0 0 1-1 1A17 17 0 0 1 3 4a1 1 0 0 1 1-1h3.5a1 1 0 0 1 1 1c0 1.25.2 2.45.57 3.57a1 1 0 0 1-.25 1z"/></svg>
        <span>0412 506 218</span>
      </li>
      <li>
        <svg viewBox="0 0 24 24" aria-hidden="true"><rect x="2" y="5" width="20" height="14" rx="2" fill="#fff"/><path d="M3 6l9 7 9-7" fill="none" stroke="var(--card-pink)" stroke-width="1.8"/></svg>
        <span>maren@pindlesbakery.com.au</span>
      </li>
      <li>
        <svg viewBox="0 0 24 24" aria-hidden="true" fill="none" stroke="#fff" stroke-width="1.8"><circle cx="12" cy="12" r="9.5"/><ellipse cx="12" cy="12" rx="4" ry="9.5"/><path d="M2.5 12h19M4 7h16M4 17h16"/></svg>
        <span>www.pindlesbakery.com.au</span>
      </li>
      <li class="company-number">ACN 581 246 037,</li>
    </ul>
  </div>
</body>
</html>
```